Book Cover for Gym Mentor for Men

My name is Mavis Dell Oakes. I am a female Gym Mentor for Men.
I need a new Book Cover Design for my second book and a back of the book.
Both with updated text.
#A… Book Cover… I like the bright red and yellow colors.
I like the weight rack and the bold headline Font
#B… Book Cover…I like the full frontal sexier body. I don not like the font style.
I want the new design sexier; super sexy. Even more eye catching for guys.
I want to push the envelope to the point of almost too much sexy.
An Brindlex book 6”x9”, 150 pages

Target Market(s)

Men

Industry/Entity Type

Health and fitness for men

Colors
FFF300
FFF600
FEFA6F
FFFEC7
FFFEE8
EB3D1F
EC4F4E
F09395
F8D3D4
FCEDEE

Requirements
Must have
• Sexy & eye catching.

```html
<!DOCTYPE html>
<html lang="en">
<head>
<meta charset="utf-8">
<title>Gym Mentor for Men – Volume II – Front and Back Cover</title>
<link rel="stylesheet" href="https://fonts.googleapis.com/css2?family=Oswald:wght@500;600;700&family=Open+Sans:wght@400;600;700;800&display=swap">
<style>
  :root {
    --bg: #3a3b3e;
    --yellow: #f7c800;
    --yellow-bright: #fff300;
    --red: #e3232b;
    --black: #141414;
    --white: #ffffff;
    --skin-light: #c98a5c;
    --skin-dark: #8a5233;
    --ink: #5a1a10;
  }
  * { box-sizing: border-box; margin: 0; padding: 0; }
  html, body { width: 1200px; height: 857px; overflow: hidden; }
  body {
    background: var(--bg);
    font-family: "Open Sans", Arial, sans-serif;
    position: relative;
  }
  .cover {
    position: absolute;
    top: 38px;
    width: 520px;
    height: 780px;
    background: var(--yellow);
    overflow: hidden;
  }
  .cover--front { left: 60px; }
  .cover--back { left: 620px; }

  /* FRONT */
  .front-photo {
    position: absolute;
    left: 211px; top: 0;
    width: 309px; height: 780px;
    background: linear-gradient(160deg, var(--skin-light) 0%, var(--skin-dark) 100%);
  }
  .author-band {
    position: absolute; left: 0; top: 8px;
    width: 222px; height: 78px;
    background: var(--red);
    display: flex; align-items: center;
    padding-left: 24px;
    z-index: 2;
  }
  .author-band span {
    font-family: "Oswald", sans-serif; font-weight: 600;
    color: var(--white); font-size: 27px; letter-spacing: .2px;
  }
  .title {
    position: absolute; left: 26px; top: 92px;
    font-family: "Oswald", sans-serif; font-weight: 700;
    line-height: .92; text-transform: uppercase;
    z-index: 2;
  }
  .title .t-gym { display: block; color: var(--black); font-size: 54px; }
  .title .t-mentor {
    display: block; color: var(--red); font-size: 78px; margin-left: 26px;
    text-shadow: 2px 2px 0 var(--yellow), -2px -2px 0 var(--yellow), 2px -2px 0 var(--yellow), -2px 2px 0 var(--yellow);
  }
  .title .t-for { color: var(--black); font-size: 56px; vertical-align: top; margin-right: 8px; }
  .title .t-men {
    color: var(--red); font-size: 124px; line-height: .85;
    text-shadow: 3px 3px 0 var(--yellow), -3px -3px 0 var(--yellow), 3px -3px 0 var(--yellow), -3px 3px 0 var(--yellow);
  }
  .promise-band {
    position: absolute; left: 0; top: 330px;
    width: 272px; height: 176px;
    background: var(--red);
    padding: 12px 0 0 26px;
    font-family: "Open Sans", sans-serif; font-weight: 800;
    text-transform: uppercase; line-height: 1;
    z-index: 2;
  }
  .promise-band .p-helping { display: block; color: var(--white); font-size: 24px; }
  .promise-band .p-hot { display: block; color: var(--white); font-size: 43px; margin-top: 2px; }
  .promise-band .p-pair { display: flex; align-items: center; margin-top: 2px; }
  .promise-band .p-words { color: var(--yellow-bright); font-size: 28px; line-height: 1.05; }
  .promise-band .p-words span:last-child { font-size: 34px; }
  .promise-band .p-amp { color: var(--yellow-bright); font-size: 78px; margin-left: 4px; line-height: .9; }
  .results {
    position: absolute; left: 24px; top: 516px;
    font-family: "Open Sans", sans-serif; font-weight: 800;
    text-transform: uppercase; line-height: .95;
    color: var(--black);
    z-index: 2;
  }
  .results .r-red { color: var(--red); }
  .results .r-1 { font-size: 21px; }
  .results .r-1 .r-red { font-size: 28px; }
  .results .r-2 { font-size: 26px; }
  .results .r-3 { font-size: 32px; }
  .results .r-3 small { font-size: 24px; color: var(--black); }
  .results .r-4 { font-size: 33px; color: var(--red); }
  .results .r-5 { display: flex; align-items: center; margin-top: -2px; }
  .results .r-amp { color: var(--red); font-size: 60px; line-height: .85; margin-right: 4px; }
  .results .r-last { font-size: 23px; line-height: 1; }
  .volume-bar {
    position: absolute; left: 0; bottom: 0;
    width: 211px; height: 44px;
    background: var(--black);
    display: flex; align-items: center; justify-content: center;
    color: var(--white); font-weight: 700; font-size: 17px;
    z-index: 2;
  }

  /* BACK */
  .back-intro {
    position: absolute; left: 26px; right: 26px; top: 26px;
    text-align: center; color: var(--ink);
    font-size: 10.5px; font-weight: 600; line-height: 1.45;
  }
  .back-band {
    position: absolute; left: 0; right: 0; top: 140px;
    height: 100px; background: var(--red);
    text-align: center; padding-top: 10px;
    font-weight: 700; line-height: 1.2;
  }
  .back-band .b-white { color: var(--white); font-size: 17px; }
  .back-band .b-yellow { color: var(--yellow-bright); font-size: 17px; }
  .back-body {
    position: absolute; left: 26px; right: 26px; top: 252px;
    text-align: center; color: var(--black);
    font-size: 10.5px; font-weight: 600; line-height: 1.45;
  }
  .back-body p + p { margin-top: 8px; }
  .back-heading {
    font-family: "Oswald", sans-serif; font-weight: 600;
    color: var(--red); text-transform: uppercase;
    font-size: 25px; line-height: 1.1; margin: 12px 0 8px;
  }
  .back-quotes { font-size: 10.5px; }
  .back-claim {
    font-family: "Oswald", sans-serif; font-weight: 600;
    color: var(--red); text-transform: uppercase;
    font-size: 15px; line-height: 1.2; margin: 10px 0 6px;
  }
  .back-close { font-size: 12px; font-weight: 700; }
  .back-footer {
    position: absolute; left: 0; right: 0; bottom: 0;
    height: 120px; background: var(--black);
    color: var(--white);
    padding: 22px 0 0 26px;
  }
  .back-footer .f-name { font-family: "Oswald", sans-serif; font-weight: 600; font-size: 22px; color: var(--white); }
  .back-footer .f-title { font-size: 12px; color: #bbbbbb; letter-spacing: .3px; }
  .back-footer .f-ask { font-size: 12px; font-weight: 600; margin-top: 18px; color: #e6e6e6; }
  .author-photo {
    position: absolute; right: 20px; bottom: 12px;
    width: 104px; height: 104px;
    border: 4px solid var(--yellow);
    background: linear-gradient(150deg, #e7d6c4 0%, #b98a62 55%, #6b4a32 100%);
  }
</style>
</head>
<body>

<section class="cover cover--front" aria-label="Front cover">
  <div class="front-photo" role="img" aria-label="Photo of a toned, tanned torso in a red strappy bikini dusted with gym chalk"></div>

  <div class="author-band"><span>MAVIS DELL OAKES</span></div>

  <h1 class="title">
    <span class="t-gym">Gym</span>
    <span class="t-mentor">Mentor</span>
    <span class="t-for">For</span><span class="t-men">Men</span>
  </h1>

  <div class="promise-band">
    <span class="p-helping">Helping Guys</span>
    <span class="p-hot">Get Hot</span>
    <div class="p-pair">
      <div class="p-words"><span>Sweaty</span><br><span>Hard</span></div>
      <span class="p-amp">&amp;</span>
    </div>
  </div>

  <div class="results">
    <div class="r-1">So <span class="r-red">Pounds</span></div>
    <div class="r-2">Melt Away</div>
    <div class="r-3"><span class="r-red">Your</span> <small>Gut</small></div>
    <div class="r-4">Shrinks</div>
    <div class="r-5"><span class="r-amp">&amp;</span><span class="r-last">You Last<br>Longer</span></div>
  </div>

  <div class="volume-bar">Volume II</div>
</section>

<section class="cover cover--back" aria-label="Back cover">
  <p class="back-intro">I’ve Been Using Eye Candy To Get Guys Interested In Health And Fitness Since The Day I Walked In The Gym And Turned Heads. I Figured If You Wanted Tits &amp; Ass I’d Give It To You. Enough To Make A Buck And Get My Guys Healthier. As A Personal Trainer For Men I’ve Learned…that Not All Guys Are The Same. Each Of You Is Different And You Need To Find What Works For You. When You Do… The Pounds Melt Away, Your Gut Shrinks, And Your Health Improves.</p>

  <div class="back-band">
    <div class="b-white">You’ll love the new you. Your girlfriend will<br>love it. Your wife will love it.</div>
    <div class="b-yellow">Nothing a woman loves more than a long<br>rock hard man in shape.</div>
  </div>

  <div class="back-body">
    <p>While everybody in the fitness community screams and yells about gym memberships, 30-day challenges, and complete diet changes … My Guys don’t do all that. My Guys are Real Men with Real bodies. Real Men that work for a living and don’t have time to live in the gym.</p>
    <p>Real men are tired of gym rats with “Look at me” egos, God given 1% body fat and abs you’ll never get. These guys are full of Shit! And they’re the first one to buy my book. Yagotta love it</p>

    <h2 class="back-heading">You Need To Find What Works For You.</h2>

    <p class="back-quotes">“I made a few adjustment in my meals added a minimum amount of exercise and lost 17 pounds in three months. Thanks Mavis. Couldn’t have done it without you.” “I took your bait and it actually made sense. Can’t believe you got me exercising. My belt shrank and had to buy new pants. Best 20 bucks I ever spent.” “I’ve tried a few expensive programs but your Prime Routine was all I ever needed. You’re right. No gym needed here.” “Strategically eating Fast food is genius. Never thought I could still eat what I love and lose weight. WOW!” “My increasing weight was scaring the hell out of me. Now I see that it’s the little changes I can do…that has changed everything.” “Every time I tried to make big drastic changes in my life. I can’t do that. All these little ‘Tricks of the Trade’ I can do.” Thank you Mavis.”</p>

    <h3 class="back-claim">Men can be fit, healthy and in shape no matter<br>their size, weight, or body fat.</h3>

    <p class="back-close">Let’s get your lazy ass in shape by finding what works for you.<br>I had to get your attention first…Then that’s what I’ll do.</p>
  </div>

  <div class="back-footer">
    <div class="f-name">MAVIS DELL OAKES</div>
    <div class="f-title">GYM MENTOR FOR MEN</div>
    <div class="f-ask">Got a few bucks to Get You Hot, Sweaty, and Hard?</div>
    <div class="author-photo" role="img" aria-label="Portrait photo of the author"></div>
  </div>
</section>

</body>
</html>
```